Updated website design needed for Radiology Group, Pinecrest Valley Imaging Partners

Clean, uncluttered, updated design needed for top regional Radiology Center. Focus on personal, patient oriented design, (not clinical). Should be simple and easy to navigate, with clear CTAs. Use blues, greens and photos of people in the Central Oregon outdoors.
Uncoded, PSD design only. 2 pages: Home page and one example interior page.
reference current site: http://www.pvipxq.com/
Sites they like:
http://www.hollowbrookscan.com/
http://www.mdlq.net/handler.cfm?event=practice,main
http://www.elmtidejoint.com/

Industry/Entity Type

Medical Imaging

Number of Pages Required

2 page

Font styles to use
Sans Serif

Requirements
Must have
• Personal and patient friendly.
• Lots of white space, clean and uncluttered. Clear CTAs, such as: Patient Bill Pay, Make an Appointment, Meet Our Doctors
• Use copy and contact information from the current site.
• Use outdoor images from Central Oregon, late Winter/ Spring (snow, light colors, spring green, for example)
• Include one example interior page, either Your Exam or Meet Our Doctors
Nice to have
• The client likes:
• Meet Our Doctors slider section, and big, easy to navigate Information Center on www.elmtidejoint.com
• The personal feel of the Your Exam section on www.hollowbrookscan.com
• Blues and Greens, outdoorsy imagery
Should not have
• The client does not like:
• complex drop down menus
• clinical feel
• Do not use lorum ipsum or dummy text.
• Do not use outdoor images from other regions. Do not use Summer (hot, poolside) or Fall (red/orange leaves) images.

```html
<!DOCTYPE html>
<html lang="en">
<head>
<meta charset="utf-8">
<title>Your Exam – Pinecrest Valley Imaging Partners</title>
<link href="https://fonts.googleapis.com/css2?family=Open+Sans:wght@400;600;700&display=swap" rel="stylesheet">
<style>
:root{
  --blue:#4286f2;
  --blue-dark:#3a74d8;
  --blue-deep:#2f68c9;
  --teal:#48d8a9;
  --ink:#1f2a3a;
  --text:#4a4f57;
  --panel:#f4f5f7;
  --line:#8a8f96;
  --white:#ffffff;
}
*{margin:0;padding:0;box-sizing:border-box}
html,body{width:1200px;height:1065px;overflow:hidden;background:var(--white)}
body{font-family:"Open Sans",sans-serif;color:var(--text);position:relative}
a{color:inherit;text-decoration:none}

.topbar{height:73px;position:relative}
.brand{position:absolute;left:89px;top:14px;display:flex;align-items:center;gap:8px}
.brand-mark{width:20px;height:20px;background:var(--blue-dark)}
.brand-name{font-size:14px;font-weight:600;color:var(--ink);line-height:1.2;width:130px}
.quick-link{position:absolute;top:30px;display:flex;align-items:center;gap:6px;font-size:13px;color:var(--ink);white-space:nowrap}
.quick-link.doctors{left:588px}
.quick-link.billpay{left:752px}
.cta{position:absolute;left:903px;top:14px;width:208px;height:46px;border-radius:23px;background:var(--teal);color:var(--white);font-size:13px;display:flex;align-items:center;justify-content:center;gap:8px;white-space:nowrap}

.mainnav{position:absolute;top:73px;left:0;width:1200px;height:51px;background:var(--blue)}
.mainnav ul{list-style:none;display:flex;position:absolute;left:89px;top:0;height:51px}
.mainnav li{height:51px;display:flex;align-items:center;padding:0 13.3px;font-size:11.5px;font-weight:600;color:var(--white);white-space:nowrap}
.mainnav li.active{background:#f4f6fb;color:var(--blue);padding:0 19px}

.hero{position:absolute;top:124px;left:0;width:1200px;height:102px;background:linear-gradient(90deg,#f2f3f5 0%,#f0f1f3 45%,#e6e8eb 75%,#eceef0 100%)}
.hero h1{position:absolute;left:89px;top:38px;font-size:27px;font-weight:600;color:var(--blue)}

.intro{position:absolute;left:90px;top:257px;width:1020px;font-size:11.6px;line-height:22px}
.intro p+p{margin-top:9px}

.exam-tabs{position:absolute;left:89px;top:391px;width:217px;list-style:none;border:1px solid var(--line);border-top:none}
.exam-tabs li{height:38.5px;display:flex;align-items:center;justify-content:center;font-size:11.4px;color:var(--ink);border-top:1px solid var(--line);text-transform:uppercase}
.exam-tabs li.active{background:var(--blue-dark);color:var(--white);border-color:var(--blue-dark);position:relative;height:39.5px}
.exam-tabs li.active::after{content:"";position:absolute;right:-6px;top:15px;border-left:6px solid var(--blue-dark);border-top:5px solid transparent;border-bottom:5px solid transparent}

.exam-panel{position:absolute;left:325px;top:389px;width:786px;height:252px;background:var(--panel);padding:19px 16px 0 24px;font-size:11.6px;line-height:22px}
.exam-panel p+p{margin-top:22px}
.btn-more{position:absolute;left:20px;top:188px;width:128px;height:39px;border-radius:20px;background:var(--blue-dark);color:var(--white);font-size:11.6px;display:flex;align-items:center;justify-content:center}

.site-footer{position:absolute;top:774px;left:0;width:1200px;height:252px;background:linear-gradient(180deg,#5c8ee0 0%,#3b74d8 100%);color:var(--white)}
.fcol{position:absolute;top:28px}
.fcol h3{font-size:13.5px;font-weight:700;margin-bottom:8px}
.fcol ul{list-style:none}
.fcol li{font-size:11.8px;height:22.2px;display:flex;align-items:center;gap:8px;white-space:nowrap}
.fcol li::before{content:"";width:4px;height:4px;border:1px solid var(--white);border-radius:50%}
.contact ul{margin-top:-4px}
.contact li{height:31px}
.contact li::before{display:none}
.contact svg{width:11px;height:11px;margin-right:6px}
.copyright{position:absolute;top:1026px;left:0;width:1200px;height:39px;background:var(--blue-deep);color:var(--white);font-size:11.8px;display:flex;align-items:center;justify-content:center}
</style>
</head>
<body>
<header class="topbar">
  <a class="brand" href="#"><span class="brand-mark"></span><span class="brand-name">Pinecrest Valley Imaging Partners</span></a>
  <a class="quick-link doctors" href="#"><svg width="10" height="12" viewBox="0 0 10 12"><circle cx="5" cy="3" r="2.6" fill="#1f2a3a"/><rect x="1" y="6.5" width="8" height="5.5" rx="1.5" fill="#1f2a3a"/></svg>MEET OUR DOCTORS</a>
  <a class="quick-link billpay" href="#"><svg width="16" height="10" viewBox="0 0 16 10"><rect x="0" y="0" width="16" height="10" rx="1.5" fill="#1f2a3a"/><rect x="0" y="2.5" width="16" height="2" fill="#fff"/></svg>PATIENT BILL PAY</a>
  <a class="cta" href="#"><svg width="12" height="12" viewBox="0 0 12 12"><rect x="0.5" y="1.5" width="11" height="10" fill="none" stroke="#fff"/><line x1="0.5" y1="4" x2="11.5" y2="4" stroke="#fff"/><rect x="3" y="6" width="2" height="2" fill="#fff"/><rect x="7" y="6" width="2" height="2" fill="#fff"/></svg>MAKE AN APPOINTMENT</a>
</header>

<nav class="mainnav">
  <ul>
    <li class="active">HOME</li><li>ABOUT US</li><li>OUR SERVICES</li><li>FOR PATIENTS</li><li>OUR PHYSICIANS</li><li>FOR PHYSICIANS</li><li>PACS &amp; DOCUMENTS</li><li>APPOINTMENTS</li><li>OUR LOCATIONS</li>
  </ul>
</nav>

<section class="hero" role="img" aria-label="Soft, faded photograph of a patient resting, shown in pale greys behind the page title">
  <h1>Your Exam</h1>
</section>

<div class="intro">
  <p>PVIP is an internationally recognized leader in medical imaging services. A specialized team of physicians and staff maintain this distinction by providing the highest level of compassion and knowledge possible, prompting reports and services to be delivered in a timely manner.</p>
  <p>PVIP Interventional Radiologists are at the forefront of groundbreaking procedures and exciting new research, creating new treatment options in oncological, cardiovascular, orthopedic, and neurological disorders.</p>
</div>

<ul class="exam-tabs">
  <li class="active">Body Composition</li>
  <li>X-Ray/Fluoroscopy</li>
  <li>Breast Imaging</li>
  <li>Computed Tomography</li>
  <li>Interventional Radiology</li>
  <li>MRI</li>
  <li>Nuclear Medicine</li>
  <li>Ultrasound</li>
  <li>Varicose Veins</li>
</ul>

<article class="exam-panel">
  <p>If you are serious about your fitness and health, a number on the scale is not enough. You need the whole picture of your health. An imaging exam of your body composition—the amount of fat, lean muscle and bone in your body—is the most accurate way to know for sure if you are on track toward your fitness and weight-loss goals.</p>
  <p>A body composition exam is performed with dual-energy X-ray absorptiometry (DXA). The imaging technology uses small amounts of X-ray to capture a total image of the body. The technique measures—with pinpoint clinical accuracy—the distribution of fat, lean muscle and bone throughout the body.</p>
  <a class="btn-more" href="#">Read More</a>
</article>

<footer class="site-footer">
  <div class="fcol" style="left:88px">
    <h3>FOR PATIENTS</h3>
    <ul><li>About Your Visit</li><li>Why Choose Us?</li><li>Patient Forms</li><li>Billing and Insurance</li><li>Locations and Maps</li><li>Appointments</li></ul>
  </div>
  <div class="fcol" style="left:374px">
    <h3>FOR PATIENTS</h3>
    <ul><li>Home</li><li>About Us</li><li>Our Physicians</li><li>For Physicians</li><li>Disclaimer</li><li>HIPAA</li><li>Log-In</li></ul>
  </div>
  <div class="fcol" style="left:641px">
    <h3>FOR PATIENTS</h3>
    <ul><li>Our Services</li><li>Mammography</li><li>MRI</li><li>CT-64</li><li>X-Ray</li><li>Nuclear Medicine</li><li>PET</li><li>Ultrasound</li></ul>
  </div>
  <div class="fcol contact" style="left:906px">
    <h3>CONTACT US</h3>
    <ul>
      <li><svg viewBox="0 0 12 12"><path d="M2 1l2 0 1 3-1.5 1a7 7 0 0 0 3.5 3.5L8 7l3 1v2a1 1 0 0 1-1 1A9 9 0 0 1 1 2a1 1 0 0 1 1-1z" fill="#fff"/></svg>(555) 210-4410 - Main Line</li>
      <li><svg viewBox="0 0 12 12"><rect x="0.5" y="1.5" width="11" height="10" fill="none" stroke="#fff"/><line x1="0.5" y1="4" x2="11.5" y2="4" stroke="#fff"/></svg>(555) 210-4425 - Scheduling</li>
      <li><svg viewBox="0 0 12 12"><rect x="0" y="2" width="12" height="8" rx="1" fill="#fff"/><rect x="0" y="4" width="12" height="1.5" fill="#3f78da"/></svg>(555) 210-4437 - Billing</li>
      <li><svg viewBox="0 0 12 12"><rect x="2" y="0.5" width="8" height="11" fill="none" stroke="#fff"/><line x1="4" y1="4" x2="8" y2="4" stroke="#fff"/><line x1="4" y1="6.5" x2="8" y2="6.5" stroke="#fff"/><line x1="4" y1="9" x2="8" y2="9" stroke="#fff"/></svg>(555) 210-4452 - Medical Records</li>
    </ul>
  </div>
</footer>
<div class="copyright">© 2016 Pinecrest Valley Imaging Partners</div>
</body>
</html>
```